Simple, Professional and neat business card design for Vendralo Inc.

We're looking to re-vamp our business card design. We're a supplier of innovative feed ingredients for the North American animal agriculture industry. We are located in Lucknow, Ontario, Canada and our flagship product is a product that prevents milk fever in dairy cows when the calve, it is fed before calving and is very effective compared to other alternatives available on the market today.

Our company has Danish roots and we import all of our product from our Danish partner/manufacturer in Denmark. We like our design to embrace high professionalism while remaining neat and simple.

Target Market(s)

B2B, Feed Mills, Veterinary Clinics, Large integrators/producers,

Industry/Entity Type

Agribusiness

Contact Information for Business Card

We like the rounded corners because they make the card easy to sit in a wallet and not many use it so it makes the card stand out, just possibly something to take account for during the design.

As you can also see on the sliders below, looking for a that simple but proffesional scandinavian design.

Requirements
Nice to have
• Rounded corners
Should not have
• Too vibrant

```html
<!DOCTYPE html>
<html lang="en">
<head>
<meta charset="utf-8">
<title>Vendralo Inc. Business Card</title>
<link href="https://fonts.googleapis.com/css2?family=Open+Sans:wght@400;600;700;800&display=swap" rel="stylesheet">
<style>
  :root {
    --backdrop: #3a3b3d;
    --brand-blue: #1a5fb4;
    --brand-blue-deep: #0e4a9a;
    --brand-blue-light: #2f74c6;
    --band-dark: #2c3037;
    --paper: #f1f2f4;
    --ink: #1f2530;
    --white: #ffffff;
  }
  * { box-sizing: border-box; margin: 0; padding: 0; }
  html, body { width: 1200px; height: 962px; overflow: hidden; }
  body {
    background: var(--backdrop);
    font-family: "Open Sans", Arial, sans-serif;
    position: relative;
  }
  .card {
    position: absolute;
    left: 250px;
    width: 700px;
    height: 400px;
    border-radius: 22px;
    overflow: hidden;
    box-shadow: 0 10px 28px rgba(0,0,0,.35);
  }
  .card-front {
    top: 60px;
    background: radial-gradient(ellipse at 50% 30%, var(--brand-blue-light) 0%, var(--brand-blue) 45%, var(--brand-blue-deep) 100%);
    color: var(--white);
  }
  .card-back { top: 500px; background: var(--paper); }

  .brand {
    display: flex; align-items: center; justify-content: center; gap: 18px;
  }
  .brand-dot {
    width: 54px; height: 54px; border-radius: 50%;
    background: var(--white); opacity: .9;
  }
  .brand-name {
    font-weight: 800; font-size: 52px; letter-spacing: .5px; color: var(--white);
  }
  .card-front .brand { margin-top: 42px; }
  .tagline {
    text-align: center; font-weight: 600; font-size: 17px; line-height: 1.25; margin-top: 16px;
  }
  .features {
    position: absolute; left: 0; right: 0; bottom: 34px;
    display: flex; height: 170px;
  }
  .feature {
    flex: 1; display: flex; flex-direction: column; align-items: center; justify-content: flex-end; gap: 14px;
  }
  .feature + .feature { border-left: 2px solid rgba(255,255,255,.8); }
  .feature svg { width: 110px; height: 110px; }
  .feature-label { font-weight: 600; font-size: 19px; }

  .back-band {
    position: absolute; left: 0; right: 0; top: 0; height: 150px;
    background: radial-gradient(ellipse at 40% 20%, var(--brand-blue-light) 0%, var(--brand-blue) 55%, var(--brand-blue-deep) 100%);
    border-bottom: 12px solid var(--band-dark);
  }
  .card-back .brand { position: absolute; top: 40px; left: 0; right: 0; }
  .holder {
    position: absolute; left: 44px; top: 190px;
    color: var(--brand-blue); font-weight: 700; font-size: 34px;
  }
  .contact-list {
    list-style: none; position: absolute; left: 44px; top: 246px;
    color: var(--ink); font-size: 20px; line-height: 1.35;
  }
  .contact-list li { display: flex; gap: 12px; align-items: flex-start; }
  .contact-list svg { width: 20px; height: 20px; margin-top: 4px; flex: none; fill: var(--brand-blue); }
  .phone-list { left: auto; right: 48px; top: 210px; font-size: 22px; }
</style>
</head>
<body>

<section class="card card-front" aria-label="Card front">
  <div class="brand">
    <span class="brand-dot"></span>
    <span class="brand-name">VENDRALO INC.</span>
  </div>
  <p class="tagline">Distributor Of Innovation Feed Ingredients<br>And Other Preventative Health Products</p>
  <div class="features">
    <div class="feature">
      <svg viewBox="0 0 100 100" fill="none" stroke="#fff" stroke-width="6" stroke-linejoin="round">
        <path d="M50 6 C62 14 76 16 88 16 C88 52 76 80 50 94 C24 80 12 52 12 16 C24 16 38 14 50 6Z"/>
        <circle cx="50" cy="46" r="18" fill="#fff" stroke="none"/>
        <path d="M50 37v18M41 46h18" stroke="#1a5fb4" stroke-width="5"/>
      </svg>
      <span class="feature-label">Preventative Care</span>
    </div>
    <div class="feature">
      <svg viewBox="0 0 100 100" fill="none" stroke="#fff" stroke-width="6" stroke-linecap="round" stroke-linejoin="round">
        <path d="M22 78 A38 38 0 1 1 88 60"/>
        <path d="M50 50 L64 24" stroke-width="8"/>
        <path d="M30 26v0M50 18v0M70 26v0M22 46v0" stroke-width="7"/>
        <path d="M26 86 L44 70 L56 78 L84 52"/>
        <path d="M72 50 L86 50 L86 64" />
      </svg>
      <span class="feature-label">High- performance</span>
    </div>
    <div class="feature">
      <svg viewBox="0 0 100 100" fill="none" stroke="#fff" stroke-width="6">
        <circle cx="50" cy="50" r="42"/>
        <text x="50" y="64" text-anchor="middle" font-family="Open Sans, sans-serif" font-weight="800" font-size="40" fill="#fff" stroke="none">Rx</text>
        <path d="M80 20 L20 80"/>
      </svg>
      <span class="feature-label">Prescription- free</span>
    </div>
  </div>
</section>

<section class="card card-back" aria-label="Card back">
  <div class="back-band"></div>
  <div class="brand">
    <span class="brand-dot"></span>
    <span class="brand-name">VENDRALO INC.</span>
  </div>
  <h1 class="holder">Mikkel Sorensen</h1>
  <ul class="contact-list">
    <li><svg viewBox="0 0 20 20"><text x="10" y="16" text-anchor="middle" font-size="17" font-weight="700" font-family="Open Sans, sans-serif">@</text></svg>mikkel@vendralo.com</li>
    <li><svg viewBox="0 0 20 20"><circle cx="10" cy="10" r="8" fill="none" stroke="#1a5fb4" stroke-width="2"/><path d="M2 10h16M10 2c-4 4-4 12 0 16M10 2c4 4 4 12 0 16" fill="none" stroke="#1a5fb4" stroke-width="1.5"/></svg>www.vendralo.com</li>
    <li><svg viewBox="0 0 20 20"><path d="M10 2 L19 10 H16 V18 H12 V13 H8 V18 H4 V10 H1Z"/></svg>Box 455, Harwick, Ontario<br>Canada N0X 4K2</li>
  </ul>
  <ul class="contact-list phone-list">
    <li><svg viewBox="0 0 20 20"><rect x="5" y="1" width="10" height="18" rx="2"/><rect x="7" y="4" width="6" height="9" fill="#fff"/></svg>555-310-2471</li>
    <li><svg viewBox="0 0 20 20"><path d="M4 2 L8 2 L9 6 L7 8 C8 11 9 12 12 13 L14 11 L18 12 L18 16 C18 17 17 18 16 18 C8 18 2 12 2 4 C2 3 3 2 4 2Z"/></svg>555-310-8846</li>
    <li><svg viewBox="0 0 20 20"><circle cx="10" cy="10" r="8" fill="none" stroke="#1a5fb4" stroke-width="2"/><path d="M7 6 L9 6 L9.5 8 L8.5 9 C9 10.5 9.5 11 11 11.5 L12 10.5 L14 11 L14 13 C14 13.5 13.5 14 13 14 C9 14 6 11 6 7 C6 6.5 6.5 6 7 6Z"/></svg>800-555-0192</li>
    <li><svg viewBox="0 0 20 20"><rect x="5" y="2" width="10" height="5"/><rect x="2" y="7" width="16" height="7" rx="1"/><rect x="5" y="12" width="10" height="6" fill="#fff" stroke="#1a5fb4" stroke-width="1.5"/></svg>555-310-6630</li>
  </ul>
</section>

</body>
</html>
```